Sunridge Pilates Centre
Business Cards
Bright & Fun-filled
Maribel Foster
Owner/Certified Pilates Instructor
2847 Kestrel Dr La Mesa CA 91873
n/A
do not have until sept 20
maribel@sunridgepilatescentre.com
www.sunridgepilatescentre.com
not sure but maybe? maybe logo or a Konrad Weller Quote or??

```html
<!DOCTYPE html>
<html lang="en">
<head>
<meta charset="utf-8">
<title>Sunridge Pilates Centre – Stationery Set</title>
<link href="https://fonts.googleapis.com/css2?family=Montserrat:wght@400;600&display=swap" rel="stylesheet">
<style>
  :root{
    --ink:#1d1b18;
    --gold:#c9982a;
    --gold-light:#e0b545;
    --paper:#ffffff;
    --board-hi:#c4c4c4;
    --board-lo:#7e7e7e;
    --label:#3a3a3a;
  }
  *{margin:0;padding:0;box-sizing:border-box}
  html,body{width:1200px;height:725px;overflow:hidden}
  body{
    position:relative;
    background:radial-gradient(ellipse at 50% 45%,var(--board-hi) 0%,#a4a4a4 55%,var(--board-lo) 100%);
    font-family:"Montserrat",Arial,sans-serif;
  }
  .piece{position:absolute;overflow:hidden;box-shadow:2px 3px 6px rgba(0,0,0,.35)}
  .piece svg.wave{position:absolute;inset:0;width:100%;height:100%}
  .brand{
    position:absolute;display:flex;align-items:center;gap:5px;
    font-weight:600;color:var(--gold);white-space:nowrap;line-height:1;
  }
  .brand .dot{width:9px;height:9px;border-radius:50%;background:currentColor;flex:none}
  .brand.on-gold{color:var(--ink)}
  .brand.sm{font-size:8px}
  .brand.md{font-size:10px}
  .brand.lg{font-size:15px}
  .brand.lg .dot{width:16px;height:16px}
  .brand.stack{flex-direction:column;gap:4px;text-align:center;line-height:1.2;white-space:normal}
  .contact{position:absolute;font-size:5px;line-height:1.45;color:var(--ink);white-space:nowrap}
  .contact.light{color:var(--paper)}
  .label{position:absolute;font-size:5px;color:var(--label);white-space:nowrap;text-align:center}
</style>
</head>
<body>

<!-- Row one -->
<div class="piece card-front" style="left:60px;top:60px;width:161px;height:84px;background:var(--ink)">
  <svg class="wave" viewBox="0 0 100 100" preserveAspectRatio="none"><path d="M0 72 C30 40 62 95 100 60 L100 100 L0 100Z" fill="var(--gold)"/></svg>
  <div class="brand sm" style="left:48px;top:14px"><span class="dot"></span>Sunridge Pilates Centre</div>
</div>
<div class="label" style="left:60px;top:149px;width:161px">Business Card Front</div>

<div class="piece card-back" style="left:247px;top:60px;width:161px;height:84px;background:var(--ink)">
  <svg class="wave" viewBox="0 0 100 100" preserveAspectRatio="none"><path d="M0 80 C35 58 60 98 100 55 L100 100 L0 100Z" fill="var(--gold)"/></svg>
  <div class="contact light" style="left:10px;top:9px">Maribel Foster<br>Owner/Certified Pilates Instructor</div>
  <div class="brand sm" style="left:10px;top:30px;font-size:7px"><span class="dot"></span>Sunridge Pilates Centre</div>
</div>
<div class="label" style="left:247px;top:149px;width:161px">Business Card Back</div>

<div class="piece card-square" style="left:434px;top:60px;width:89px;height:89px;background:var(--ink)">
  <svg class="wave" viewBox="0 0 100 100" preserveAspectRatio="none"><path d="M0 75 C40 55 60 95 100 62 L100 100 L0 100Z" fill="var(--gold)"/></svg>
  <div class="brand sm stack" style="left:0;top:12px;width:89px;font-size:7px"><span class="dot"></span>Sunridge<br>Pilates Centre</div>
</div>
<div class="label" style="left:434px;top:153px;width:89px">Square Card Front</div>

<!-- Envelopes -->
<div class="envelopes" style="position:absolute;left:874px;top:65px;width:273px;height:192px">
  <svg viewBox="0 0 273 192" width="273" height="192" style="filter:drop-shadow(2px 3px 4px rgba(0,0,0,.35))">
    <polygon points="40,0 273,0 273,70 40,70" fill="var(--gold-light)"/>
    <polygon points="40,70 156,18 273,70" fill="var(--gold)"/>
    <rect x="40" y="70" width="233" height="30" fill="var(--ink)"/>
    <polygon points="22,55 273,55 273,120 22,120" fill="var(--gold-light)"/>
    <polygon points="22,120 148,78 273,120" fill="var(--gold)"/>
    <rect x="22" y="120" width="251" height="18" fill="var(--ink)"/>
    <rect x="0" y="112" width="273" height="80" fill="var(--ink)"/>
    <path d="M0 175 C90 150 170 195 273 160 L273 192 L0 192Z" fill="var(--gold)"/>
  </svg>
</div>
<div class="label" style="left:874px;top:258px;width:273px">Envelope Set</div>

<!-- Row two -->
<div class="piece card-gold" style="left:60px;top:211px;width:161px;height:87px;background:var(--gold)">
  <div class="brand md on-gold" style="left:22px;top:36px"><span class="dot"></span>Sunridge Pilates Centre</div>
</div>
<div class="label" style="left:60px;top:302px;width:161px">Business Card Gold</div>

<div class="piece card-black" style="left:247px;top:211px;width:161px;height:87px;background:var(--ink)">
  <div class="brand md" style="left:22px;top:36px"><span class="dot"></span>Sunridge Pilates Centre</div>
</div>
<div class="label" style="left:247px;top:302px;width:161px">Business Card Black</div>

<div class="piece card-slim" style="left:434px;top:230px;width:152px;height:58px;background:var(--ink)">
  <svg class="wave" viewBox="0 0 100 100" preserveAspectRatio="none"><path d="M0 70 C35 45 65 90 100 55 L100 100 L0 100Z" fill="var(--gold)"/></svg>
  <div class="brand sm" style="left:44px;top:10px;font-size:7px"><span class="dot"></span>Sunridge Pilates Centre</div>
</div>
<div class="label" style="left:434px;top:292px;width:152px">Slim Card Option</div>

<div class="piece compliment-slip" style="left:617px;top:161px;width:187px;height:101px;background:var(--ink)">
  <svg class="wave" viewBox="0 0 100 100" preserveAspectRatio="none"><path d="M0 80 C30 55 60 95 100 58 L100 100 L0 100Z" fill="var(--gold)"/></svg>
  <div class="brand sm" style="left:14px;top:16px"><span class="dot"></span>Sunridge Pilates Centre</div>
</div>
<div class="label" style="left:617px;top:266px;width:187px">Compliment Slip</div>

<!-- Letterheads -->
<div class="piece letterhead-first" style="left:60px;top:329px;width:278px;height:357px;background:var(--paper)">
  <svg class="wave" viewBox="0 0 278 357" preserveAspectRatio="none">
    <path d="M0 0 H278 V20 C200 25 120 60 0 55Z" fill="var(--ink)"/>
    <path d="M0 55 C120 60 200 25 278 20 V25 C200 32 120 66 0 62Z" fill="var(--gold)"/>
  </svg>
  <div class="brand sm" style="left:10px;top:10px;font-size:7px"><span class="dot"></span>Sunridge Pilates Centre</div>
  <div class="contact" style="right:10px;top:40px;text-align:right">2847 Kestrel Dr La Mesa CA 91873<br>www.sunridgepilatescentre.com</div>
</div>
<div class="label" style="left:60px;top:690px;width:278px">Letterhead Page One</div>

<div class="piece letterhead-second" style="left:374px;top:329px;width:262px;height:357px;background:var(--paper)">
  <svg class="wave" viewBox="0 0 262 357" preserveAspectRatio="none">
    <path d="M0 298 C90 300 170 270 262 245 V250 C170 276 90 306 0 304Z" fill="var(--gold)"/>
    <path d="M0 304 C90 306 170 276 262 250 V357 H0Z" fill="var(--ink)"/>
  </svg>
  <div class="brand sm" style="left:12px;top:322px;font-size:7px"><span class="dot"></span>Sunridge Pilates Centre</div>
  <div class="contact light" style="left:120px;top:338px">2847 Kestrel Dr La Mesa CA 91873</div>
</div>
<div class="label" style="left:374px;top:690px;width:262px">Letterhead Page Two</div>

<!-- Presentation folder -->
<div class="folder" style="position:absolute;left:701px;top:341px;width:451px;height:355px">
  <svg viewBox="0 0 451 355" width="451" height="355" style="position:absolute;inset:0;filter:drop-shadow(2px 3px 5px rgba(0,0,0,.35))">
    <rect x="0" y="0" width="451" height="200" fill="var(--ink)"/>
    <path d="M0 150 C140 90 260 200 451 110 V200 H0Z" fill="var(--gold)"/>
    <path d="M0 200 H451 V290 H300 L290 355 H170 L160 290 H0Z" fill="var(--gold)"/>
    <line x1="0" y1="200" x2="451" y2="200" stroke="var(--ink)" stroke-width="1"/>
    <rect x="310" y="300" width="60" height="32" fill="var(--ink)"/>
    <path d="M310 322 C330 314 350 330 370 318 V332 H310Z" fill="var(--gold)"/>
  </svg>
  <div class="brand lg" style="left:210px;top:50px"><span class="dot"></span>Sunridge Pilates Centre</div>
  <div class="contact light" style="left:300px;top:178px">2847 Kestrel Dr La Mesa CA 91873</div>
  <div class="contact" style="left:180px;top:262px">www.sunridgepilatescentre.com</div>
</div>
<div class="label" style="left:1010px;top:700px;width:130px">Presentation Folder</div>

</body>
</html>
```